依頼詳細
学校営業チームが養成校にグループ会社になったことを知らせるためのチラシ。
ミナモリーフの保育園は絵本に力をいれており、2500冊の絵本がある図書館があり、
ロワ・ホールディングスの保育園は主体性保育を行っています。そのことを記載していただくことと、HPを参考にしていただき両会社の園一覧を載せていただきたいです。
ミナモリーフ https://minamo-leaf.example.jp/recruit/?ym=2023-9#calendar
ロワ・ホールディングス https://lowa-hd.example.jp/
記載項目
ひかりの芽をそだてる ソラエ保育グループ株式会社
住所:987-0002 東京都葛飾区青葉台9-2-5
TEL:03-5918-4470 FAX03-3602-2192

※添付の絵本の図書館の写真を使用していただきたい

サイズ
A4
ページ数
片面
希望イメージ
シンプル 複雑
単色 カラフル
暗い 明るい
日常 高級
遊び心 厳粛
未来的 伝統的
女性的 男性的
希望する色
赤系、黄・オレンジ系
納品ファイル
• 高解像度JPG (.jpg)
• イラストレーター形式 (.ai)
■ 選んだ理由

保育園らしい可愛いデザインが気に入り、情報が見やすかった点

■ 提案者全員のお礼・コメント

たくさんの応募ありがとうございました!魅力的なデザインも多かったです。

```html
<!DOCTYPE html>
<html lang="ja">
<head>
<meta charset="utf-8">
<title>保育企業合併のお知らせ</title>
<link rel="stylesheet" href="https://fonts.googleapis.com/css2?family=M+PLUS+Rounded+1c:wght@500;700;800&display=swap">
<style>
:root{
  --pink:#e8577a;
  --pink-band:#f08e9c;
  --pink-soft:#fde3e6;
  --pink-line:#f4b5c0;
  --yellow:#fde98d;
  --yellow-soft:#fff6c8;
  --brown:#5a3a2a;
  --text:#4a3a33;
  --white:#ffffff;
  --orange:#f7a642;
}
*{box-sizing:border-box;margin:0;padding:0}
html,body{width:851px;height:1200px;overflow:hidden}
body{font-family:"M PLUS Rounded 1c",sans-serif;color:var(--text);background:var(--white)}
.flyer{position:relative;width:851px;height:1200px;overflow:hidden;background:var(--pink-soft)}

.notice-band{position:absolute;left:0;top:0;width:851px;height:58px;background:var(--pink-band)}
.notice-label{position:absolute;left:26px;top:12px;color:var(--white);font-weight:800;font-size:24px;letter-spacing:2px}

.illustration{position:absolute;border-radius:16px}
.scene-top{left:20px;top:68px;width:811px;height:166px;background:linear-gradient(90deg,#fbe3c4,#fde6d8 50%,#fde9b8)}

.title-panel{position:absolute;left:24px;top:244px;width:803px;height:190px;background:var(--white);border-radius:20px;text-align:center}
.title-lead{margin-top:14px;font-size:30px;font-weight:800;color:var(--brown);letter-spacing:2px}
.title-main{font-size:58px;font-weight:800;color:var(--pink);line-height:1.12;letter-spacing:1px}

.merge{position:absolute;left:0;top:450px;width:851px;height:492px;background:var(--yellow)}
.card{position:absolute;top:16px;width:384px;height:462px;background:var(--white);border-radius:18px;overflow:hidden}
.card-left{left:22px}
.card-right{left:445px}
.card-art{position:absolute}
.photo{left:120px;top:14px;width:150px;height:150px;border-radius:50%}
.photo-library{background:linear-gradient(135deg,#e9d3b4,#c79b6e)}
.photo-play{background:linear-gradient(135deg,#cfe6c6,#9ccc9a)}
.kid{top:92px;width:86px;height:76px;border-radius:14px}
.kid-reading{left:14px;background:#f6c4b4}
.kid-playing{left:284px;background:#f8c98e}
.bubble{position:absolute;font-size:11px;font-weight:700;line-height:1.5;color:var(--text);background:var(--pink-soft);border-radius:12px;padding:6px 8px}
.bubble-a{left:10px;top:14px;width:104px}
.bubble-b{left:276px;top:14px;width:100px}
.bubble-c{left:14px;top:174px;width:356px;text-align:center;background:var(--yellow-soft)}
.company{position:absolute;left:0;top:212px;width:100%;text-align:center;border-top:2px dashed var(--pink-line);padding-top:6px}
.company-kind{font-size:16px;font-weight:800;color:var(--pink)}
.company-name{font-size:34px;font-weight:800;color:var(--pink);line-height:1.1;white-space:nowrap}
.company-name.long{font-size:29px;line-height:1.29}
.nursery-list{position:absolute;left:12px;right:12px;top:290px;bottom:12px;background:var(--yellow-soft);border-radius:10px;padding:8px 10px;font-size:10.5px;line-height:1.55;font-weight:500}
.list-head{display:inline-block;background:var(--orange);color:var(--white);font-weight:800;border-radius:4px;padding:0 6px;margin-right:4px}
.plus{position:absolute;left:404px;top:224px;width:44px;height:44px}

.contact{position:absolute;left:0;top:942px;width:851px;height:258px;background:var(--pink-soft)}
.contact-label{position:absolute;left:345px;top:14px;width:160px;height:32px;border-radius:16px;background:var(--pink);color:var(--white);font-size:17px;font-weight:800;text-align:center;line-height:32px}
.contact-box{position:absolute;left:180px;top:58px;width:490px;height:170px;text-align:center;color:var(--brown)}
.contact-lead{font-size:22px;font-weight:800}
.contact-name{font-size:34px;font-weight:800;line-height:1.3}
.contact-line{font-size:17px;font-weight:700;margin-top:6px}
.scene-balloon{left:26px;top:20px;width:130px;height:220px;background:#e9c3d6}
.scene-kids-bottom{left:700px;top:90px;width:130px;height:150px;background:#f8cfb0}
</style>
</head>
<body>
<main class="flyer">
  <header class="notice-band"><p class="notice-label">保育企業合併のお知らせ</p></header>

  <div class="illustration scene-top" role="img" aria-label="虹と太陽と雲の空の下で手をつなぐ子どもたちのイラスト"></div>

  <section class="title-panel">
    <p class="title-lead">ひかりの芽をそだてる</p>
    <h1 class="title-main">ソラエ保育グループ<br>株式会社になります</h1>
  </section>

  <section class="merge">
    <article class="card card-left">
      <p class="bubble bubble-a">これからを生きる子どもたちに本の楽しさを伝えます</p>
      <div class="card-art photo photo-library" role="img" aria-label="絵本の図書館の写真"></div>
      <p class="bubble bubble-b">毎日の読み聞かせを大切にしています</p>
      <div class="card-art kid kid-reading" role="img" aria-label="絵本を読む子どものイラスト"></div>
      <p class="bubble bubble-c">絵本に力を入れており、2500冊の絵本がある図書館があります</p>
      <div class="company">
        <p class="company-kind">株式会社</p>
        <h2 class="company-name">ミナモリーフ</h2>
      </div>
      <div class="nursery-list">
        <span class="list-head">園一覧</span>東京都葛飾区ほか<br>
        【認可保育所】ミナモリーフ保育園 青葉台／ミナモリーフ保育園 若葉町<br>
        ミナモリーフ保育園 桜ヶ丘／ミナモリーフ保育園 川辺<br>
        【小規模保育】ミナモリーフ 小さなおうち 青葉台／ミナモリーフ 小さなおうち 緑町<br>
        ミナモリーフ 小さなおうち 東口／ミナモリーフ 小さなおうち 南口<br>
        【企業主導型】ミナモリーフ キッズルーム 本町
      </div>
    </article>

    <svg class="plus" viewBox="0 0 44 44" aria-hidden="true"><circle cx="22" cy="22" r="22" fill="#e8577a"/><path d="M22 11v22M11 22h22" stroke="#fff" stroke-width="6" stroke-linecap="round"/></svg>

    <article class="card card-right">
      <p class="bubble bubble-a">心の安定と主体性を育む保育をしています</p>
      <div class="card-art photo photo-play" role="img" aria-label="園で遊ぶ子どもたちの写真"></div>
      <p class="bubble bubble-b">一人ひとりの「やりたい」を見守ります</p>
      <div class="card-art kid kid-playing" role="img" aria-label="遊ぶ子どものイラスト"></div>
      <p class="bubble bubble-c">子どもが自ら選び、考え、行動する主体性保育を行っています</p>
      <div class="company">
        <p class="company-kind">株式会社</p>
        <h2 class="company-name long">ロワ・ホールディングス</h2>
      </div>
      <div class="nursery-list">
        <span class="list-head">園一覧</span>東京都・千葉県ほか<br>
        【認可保育所】ロワ保育園 青葉台／ロワ保育園 川の手／ロワ保育園 北町<br>
        ロワ保育園 西が丘／ロワ保育園 港南／ロワ保育園 花見台<br>
        【小規模保育】ロワ ちいさな森 東町／ロワ ちいさな森 中央<br>
        【認証保育所】ロワ キッズガーデン 駅前／ロワ キッズガーデン 本通り<br>
        【学童保育】ロワ 放課後クラブ 青葉台
      </div>
    </article>
  </section>

  <footer class="contact">
    <div class="illustration scene-balloon" role="img" aria-label="気球に乗る子どもたちのイラスト"></div>
    <p class="contact-label">お問い合わせ</p>
    <div class="contact-box">
      <p class="contact-lead">ひかりの芽をそだてる</p>
      <p class="contact-name">ソラエ保育グループ株式会社</p>
      <p class="contact-line">【住所】〒987-0002 東京都葛飾区青葉台9-2-5</p>
      <p class="contact-line">【TEL】03-5918-4470 【FAX】03-5918-4471</p>
    </div>
    <div class="illustration scene-kids-bottom" role="img" aria-label="手を振る子どものイラスト"></div>
  </footer>
</main>
</body>
</html>
```